New funky, super creative logo design for printing business

Stamp, Wrap and Ship

We are a new digital printing business, based on the Gold Coast of Australia. We have a web site under construction - www.stampwrapandship.net, which will aim at the Business to Business market. We are digital printers, offering a wide variety of print products from business cards to wide format print jobs for consumers and small to medium sized business'. We offer up to date technological, digital and wide format print, at hi octane speed. Our prices are very competitive, and turnaround is super fast.

We like to think outside the box, and this should shine through in the design and colours that you use. Be bold and creative, we want to stand out from the crowd.

We will also soon be needing a full suite of marketing collaterals - posters, letterheads, scrap pads, calendars, banners etc. but this will come later, once we have decided on the logo and layouts.

We want a vibrant, bold image, communicating vibrancy and excitement.

Details on the card are company name: Stamp, Wrap and Ship.
www.stampwrapandship.net.
contact: Corinne (+61)437182265
e-mail:corinne@stampwrapandship.net

I must be able to change some of the details such as the name and number on the card.

Target Market(s)

Business to business, small retail, some individuals

Industry/Entity Type

Construction

Requirements
Must have
• Unique funky logo.
Nice to have
• A three dimensional look,with depth in the logo.

```html
<!DOCTYPE html>
<html lang="en">
<head>
<meta charset="utf-8">
<title>Stamp, Wrap and Ship – Business Card</title>
<link rel="stylesheet" href="https://fonts.googleapis.com/css2?family=Noto+Sans:wght@400&family=Quicksand:wght@600&display=swap">
<style>
  :root {
    --card-bg: #060807;
    --ink-white: #ffffff;
    --ink-cyan: #2ef3f6;
    --ink-magenta: #f51af0;
    --ink-yellow: #f7f51c;
    --divider: #8a8a8a;
  }
  html, body {
    margin: 0;
    padding: 0;
    overflow: hidden;
    background: var(--card-bg);
  }
  .card {
    position: relative;
    width: 1200px;
    height: 734px;
    background: var(--card-bg);
    overflow: hidden;
    font-family: "Noto Sans", Arial, sans-serif;
    color: var(--ink-white);
  }
  .brand {
    position: absolute;
    left: 0;
    right: 0;
    top: 205px;
    display: flex;
    justify-content: center;
    align-items: center;
    gap: 18px;
  }
  .brand-mark {
    width: 34px;
    height: 34px;
    background: var(--ink-magenta);
  }
  .brand-name {
    font-family: "Quicksand", Arial, sans-serif;
    font-weight: 600;
    font-size: 54px;
    line-height: 1;
    color: var(--ink-cyan);
    letter-spacing: -0.5px;
  }
  .contact-name {
    position: absolute;
    left: 105px;
    top: 372px;
    font-size: 39px;
    line-height: 1.2;
  }
  .divider {
    position: absolute;
    left: 362px;
    top: 341px;
    width: 3px;
    height: 159px;
    background: var(--divider);
  }
  .contact-details {
    position: absolute;
    right: 108px;
    top: 340px;
    text-align: right;
    font-size: 29px;
    line-height: 39px;
    letter-spacing: 0.3px;
  }
  .contact-details p { margin: 0; }
  .contact-details .web { margin-top: 47px; }
  .pixel-band {
    position: absolute;
    left: 17px;
    top: 604px;
    width: 1166px;
    height: 94px;
    background: linear-gradient(90deg, var(--ink-cyan), var(--ink-magenta), var(--ink-yellow), var(--ink-cyan), var(--ink-magenta), var(--ink-yellow));
    opacity: 0.85;
  }
</style>
</head>
<body>
  <main class="card">
    <header class="brand">
      <span class="brand-mark" aria-hidden="true"></span>
      <span class="brand-name">Stamp, Wrap and Ship</span>
    </header>

    <p class="contact-name" style="margin:0">Corinne</p>
    <div class="divider" aria-hidden="true"></div>

    <section class="contact-details">
      <p class="phone">Phone: (+61)437182265</p>
      <p class="email">Email: corinne@stampwrapandship.net</p>
      <p class="web">www.stampwrapandship.net</p>
    </section>

    <div class="pixel-band" role="img" aria-label="Decorative row of pixel-block letters in cyan, magenta and yellow"></div>
  </main>
</body>
</html>
```